Bref créative
Business Cards and Stationery for The Cheerful Parcel
The Cheerful Parcel
Traditional
Nora Whitcomb
Chief Executive Officer
24817 Halvern
Dunmore, MI 4735-1186
nora@thecheerfulparcel.example
www.thecheerfulparcel.example
This is my logo in AI

```html
<!DOCTYPE html>
<html lang="en">
<head>
<meta charset="utf-8">
<title>The Cheerful Parcel – Business Card</title>
<link rel="stylesheet" href="https://fonts.googleapis.com/css2?family=Montserrat:wght@400;600;700&family=Open+Sans:wght@400;600&display=swap">
<style>
:root{
  --plum:#7a1d6c;
  --rose:#f1a6b6;
  --rose-soft:#f9d6de;
  --ink:#4a4a4a;
  --paper:#ffffff;
  --backdrop:#e9e9ea;
}
*{margin:0;padding:0;box-sizing:border-box}
html,body{width:1200px;height:984px;overflow:hidden;background:var(--backdrop)}
.sheet{width:1200px;height:984px;display:flex;flex-direction:column;align-items:center;justify-content:center;gap:40px}
.card{position:relative;width:760px;height:434px;background:var(--paper);border-radius:22px;overflow:hidden;box-shadow:0 6px 18px rgba(0,0,0,.12)}

/* back side */
.card-back{display:flex;flex-direction:column;align-items:center;justify-content:center;gap:34px}
.brand{display:flex;align-items:center;gap:14px}
.brand-mark{width:30px;height:30px;background:var(--rose);border-radius:4px}
.brand-name{font-family:"Montserrat",sans-serif;font-weight:600;color:var(--plum);font-size:34px;letter-spacing:.5px}
.back-url{font-family:"Montserrat",sans-serif;font-size:13px;letter-spacing:5px;color:var(--plum)}

/* front side */
.wave{position:absolute;inset:0;width:100%;height:100%}
.identity{position:absolute;left:50px;top:60px;width:390px;display:flex;flex-direction:column;align-items:center;gap:14px}
.identity .brand-name{font-size:34px;text-align:center;line-height:1.15}
.tagline{font-family:"Montserrat",sans-serif;font-size:17px;letter-spacing:2px;color:var(--rose);font-weight:600}
.divider{position:absolute;left:462px;top:56px;width:2px;height:190px;background:var(--rose)}
.contact{position:absolute;left:490px;top:54px;width:250px}
.person-name{font-family:"Montserrat",sans-serif;font-weight:700;color:var(--plum);font-size:17px}
.person-title{font-family:"Open Sans",sans-serif;font-size:11.5px;color:var(--ink);margin:2px 0 12px}
.details{list-style:none;font-family:"Open Sans",sans-serif;font-size:11.5px;color:var(--ink);line-height:1.35}
.details li{display:flex;align-items:flex-start;gap:8px;margin-bottom:4px}
.icon{flex:0 0 16px;width:16px;height:16px;margin-top:1px}
</style>
</head>
<body>
<main class="sheet">

  <section class="card card-back" aria-label="Card back">
    <div class="brand">
      <span class="brand-mark"></span>
      <span class="brand-name">The Cheerful Parcel</span>
    </div>
    <p class="back-url">www.thecheerfulparcel.example</p>
  </section>

  <section class="card card-front" aria-label="Card front">
    <svg class="wave" viewBox="0 0 760 434" preserveAspectRatio="none" aria-hidden="true">
      <path d="M0 300 C180 270 330 330 480 355 C600 375 700 372 760 360 L760 434 L0 434 Z" fill="var(--plum)"/>
      <path d="M0 286 C180 256 330 318 480 343 C600 363 700 360 760 348" fill="none" stroke="var(--rose)" stroke-width="7"/>
      <path d="M0 275 C180 245 330 307 480 332 C600 352 700 349 760 337" fill="none" stroke="var(--rose-soft)" stroke-width="2"/>
    </svg>

    <div class="identity">
      <span class="brand-name">The Cheerful Parcel</span>
      <span class="tagline">Uplifting gifts for women</span>
    </div>

    <div class="divider"></div>

    <div class="contact">
      <h1 class="person-name">Nora Whitcomb</h1>
      <p class="person-title">Chief Executive Officer</p>
      <ul class="details">
        <li>
          <svg class="icon" viewBox="0 0 16 16"><circle cx="8" cy="8" r="8" fill="var(--plum)"/><path d="M8 3.5a2.6 2.6 0 0 0-2.6 2.6c0 2 2.6 5.2 2.6 5.2s2.6-3.2 2.6-5.2A2.6 2.6 0 0 0 8 3.5z" fill="#fff"/><circle cx="8" cy="6.1" r="1" fill="var(--plum)"/></svg>
          <span>24817 Halvern<br>Dunmore, MI 4735-1186</span>
        </li>
        <li>
          <svg class="icon" viewBox="0 0 16 16"><circle cx="8" cy="8" r="8" fill="var(--plum)"/><path d="M5 4.2l1.6-.2.8 2-1 .8a6 6 0 0 0 2.8 2.8l.8-1 2 .8-.2 1.6c-3.8.4-7.2-3-6.8-6.8z" fill="#fff"/></svg>
          <span>(734) 555-0126</span>
        </li>
        <li>
          <svg class="icon" viewBox="0 0 16 16"><circle cx="8" cy="8" r="8" fill="var(--plum)"/><rect x="5.5" y="3.5" width="5" height="9" rx="1" fill="#fff"/><circle cx="8" cy="11.2" r=".6" fill="var(--plum)"/></svg>
          <span>(313) 555-0178</span>
        </li>
        <li>
          <svg class="icon" viewBox="0 0 16 16"><circle cx="8" cy="8" r="8" fill="var(--plum)"/><rect x="4" y="5" width="8" height="6" rx=".8" fill="#fff"/><rect x="5.5" y="3.5" width="5" height="2" fill="#fff"/></svg>
          <span>(734) 555-0193</span>
        </li>
        <li>
          <svg class="icon" viewBox="0 0 16 16"><circle cx="8" cy="8" r="8" fill="var(--plum)"/><path d="M4 5h8v5H7l-2 2v-2H4z" fill="#fff"/></svg>
          <span>The_Cheerful_Parcel</span>
        </li>
        <li>
          <svg class="icon" viewBox="0 0 16 16"><circle cx="8" cy="8" r="8" fill="var(--plum)"/><rect x="4" y="5" width="8" height="6" fill="#fff"/><path d="M4 5l4 3.2L12 5" fill="none" stroke="var(--plum)" stroke-width=".9"/></svg>
          <span>nora@thecheerfulparcel.example</span>
        </li>
        <li>
          <svg class="icon" viewBox="0 0 16 16"><circle cx="8" cy="8" r="8" fill="var(--plum)"/><circle cx="8" cy="8" r="4" fill="none" stroke="#fff" stroke-width="1"/><path d="M4 8h8M8 4c-2 2.4-2 5.6 0 8M8 4c2 2.4 2 5.6 0 8" fill="none" stroke="#fff" stroke-width=".8"/></svg>
          <span>www.thecheerfulparcel.example</span>
        </li>
      </ul>
    </div>
  </section>

</main>
</body>
</html>
```